Hardware Brand Packaging Design Project

We require a design for packaging for products in the retail hardware range. Initially this will be for a set of header cards for abrasive sanding discs but we plan to add other items to the range so we are looking for a range of brand elements that can be extended to other types of packaging.
The brand name is "Lumen Ridge" and we are looking for a black or dark grey background with a subtle fine pattern to break up the solid colour. This part of the design needs to be 'expandable' so that it can be used on different pack sizes as we increase the range. Two highlight or complimentary colours will add a bit of impact and become part of the brand style.
For printing purposes we have allowed for 4 colour process plus two spot colours and we have attached one of the header card dielines as a guide.
Target Market(s)
Home owners of both gender in the 25 to 55 age range
Industry/Entity Type
Printing
Requirements
Must have
- *The brand name "Lumen Ridge" should appear in the top left hand corner and we had in mind that the word would be a shiny metal / chrome appearance in could be in the shape of a shield or spear point but are open to any other suggestions.The word can be on one line or one above the other.
*Between the bottom of the hanger hole and the edge of the card is the words ABRASIVES & ACCESSORIES
*We want a performance guarantee device circle / seal or other in the bottom left quartile of the front facing panel. Circle device on attachment shows approx position.
* The right hand 25mm of the card is to be devoted to specific information about the product in the pack. This will be done by an adhered over-sticker ( see attached die-line No 2 )
* 3 line address panel or rear of card - QRV Abrasives, 456 Lane, West Auckland, New Zealand.
* Also somewhere on rear panel "Cut, Quality Checked & Packed in New Zealand from imported materials."
Nice to have
- It would be good, but not essential, to see a rough mock-up of how this design would transfer across to a box approx 80mm across the front, 100mm deep and 250mm high.

```html
<!DOCTYPE html>
<html lang="en">
<head>
<meta charset="utf-8">
<title>Lumen Ridge – Abrasives & Accessories Header Card</title>
<link rel="stylesheet" href="https://fonts.googleapis.com/css2?family=Bowlby+One&family=Roboto:wght@900&family=Arimo:wght@700&family=Tinos&display=swap">
<style>
  :root {
    --page: #ffffff;
    --card-top: #2e3034;
    --card-mid: #3b3e43;
    --card-bottom: #1c1d20;
    --card-texture: #ffffff;
    --swoosh: #e8160c;
    --swoosh-dark: #b50c05;
    --hanger: #ffffff;
    --headline: #f7b500;
    --headline-shadow: #6a4a00;
    --brand: #e4e8ec;
    --panel-light: #d7e6f3;
    --panel-dark: #9fc0de;
    --ink: #1a1a1a;
    --seal-gold: #f2b705;
    --seal-dark: #2a2a2a;
    --small-print: #ffffff;
  }
  html, body {
    margin: 0;
    padding: 0;
    width: 1200px;
    height: 1123px;
    overflow: hidden;
    background: var(--page);
  }
  .header-card {
    position: relative;
    width: 1200px;
    height: 1123px;
  }
  .card-art {
    position: absolute;
    inset: 0;
    width: 1200px;
    height: 1123px;
  }
  .brand-name {
    position: absolute;
    left: 40px;
    top: 630px;
    margin: 0;
    font-family: "Roboto", sans-serif;
    font-weight: 900;
    font-size: 38px;
    line-height: 1;
    color: var(--brand);
  }
  .address-panel {
    position: absolute;
    left: 40px;
    top: 140px;
    width: 344px;
    height: 117px;
    box-sizing: border-box;
    padding: 14px 18px;
    background: linear-gradient(180deg, var(--panel-dark), var(--panel-light));
    box-shadow: -4px -4px 6px rgba(0,0,0,0.55);
    transform: rotate(180deg);
    font-family: "Tinos", serif;
    font-size: 27px;
    line-height: 1.12;
    color: var(--ink);
    font-style: normal;
  }
  .address-panel span { display: block; }
  .headline {
    position: absolute;
    left: 110px;
    top: 762px;
    width: 990px;
    margin: 0;
    text-align: center;
    font-family: "Bowlby One", sans-serif;
    font-size: 57px;
    line-height: 1.1;
    letter-spacing: 1px;
    color: var(--headline);
    text-shadow: 3px 3px 0 var(--headline-shadow), 5px 5px 6px rgba(0,0,0,0.45);
  }
  .guarantee-seal {
    position: absolute;
    left: 91px;
    top: 912px;
    width: 106px;
    height: 106px;
    border-radius: 50%;
    background: var(--seal-gold);
    box-shadow: 0 2px 4px rgba(0,0,0,0.5);
  }
  .guarantee-seal::after {
    content: "";
    position: absolute;
    inset: 20px;
    border-radius: 50%;
    background: var(--seal-dark);
    border: 3px solid var(--seal-gold);
  }
  .origin-note {
    position: absolute;
    left: 54px;
    top: 1022px;
    width: 180px;
    margin: 0;
    text-align: center;
    font-family: "Arimo", sans-serif;
    font-weight: 700;
    font-size: 9.5px;
    line-height: 1.2;
    color: var(--small-print);
  }
</style>
</head>
<body>
<main class="header-card">
  <svg class="card-art" viewBox="0 0 900 842" width="1200" height="1123" aria-hidden="true">
    <defs>
      <linearGradient id="card-fill" x1="0" y1="0" x2="0" y2="1">
        <stop offset="0" stop-color="var(--card-top)"/>
        <stop offset="0.6" stop-color="var(--card-mid)"/>
        <stop offset="1" stop-color="var(--card-bottom)"/>
      </linearGradient>
      <pattern id="fine-texture" width="4" height="4" patternUnits="userSpaceOnUse" patternTransform="rotate(45)">
        <line x1="0" y1="0" x2="0" y2="4" stroke="var(--card-texture)" stroke-width="0.8" stroke-opacity="0.05"/>
      </pattern>
      <linearGradient id="swoosh-fill" x1="0" y1="0" x2="0" y2="1">
        <stop offset="0" stop-color="var(--swoosh)"/>
        <stop offset="1" stop-color="var(--swoosh-dark)"/>
      </linearGradient>
      <clipPath id="card-clip">
        <path d="M38,18 L160,18 C230,240 790,240 845,18 L857,18 Q877,18 877,38 L877,788 Q877,808 857,808 L855,808 C790,651 250,651 185,808 L38,808 Q18,808 18,788 L18,38 Q18,18 38,18 Z"/>
      </clipPath>
    </defs>
    <g class="card-body" clip-path="url(#card-clip)">
      <rect x="0" y="0" width="900" height="842" fill="url(#card-fill)"/>
      <rect x="0" y="0" width="900" height="842" fill="url(#fine-texture)"/>
      <path class="swoosh-top" fill="url(#swoosh-fill)" d="M0,10 L175,10 C290,170 560,300 862,195 C600,330 320,290 0,130 Z"/>
      <path class="swoosh-bottom" fill="url(#swoosh-fill)" d="M40,602 C280,480 620,440 885,452 L885,548 C650,478 310,508 40,602 Z"/>
    </g>
    <path class="hanger-hole" fill="var(--hanger)" d="M305,270 L540,270 Q556,270 556,288 Q556,306 540,306 L500,306 Q490,330 470,318 Q455,305 440,318 Q420,335 400,318 Q385,305 370,318 Q350,330 335,310 L265,410 L330,515 Q345,490 365,505 Q385,520 400,505 Q420,485 440,505 Q455,515 470,500 Q490,485 505,515 L540,515 Q556,515 556,533 Q556,551 540,551 L305,551 L225,425 Q215,415 210,412 Q222,406 225,398 Z"/>
  </svg>

  <address class="address-panel">
    <span>QRV Abrasives, 456 Lane,</span>
    <span>West Auckland,</span>
    <span>New Zealand.</span>
  </address>

  <p class="brand-name">Lumen Ridge</p>

  <h1 class="headline">ABRASIVES &amp; ACCESSORIES</h1>

  <div class="guarantee-seal" role="img" aria-label="Performance guarantee seal"></div>
  <p class="origin-note">Cut, Quality Checked &amp; Packed<br>in New Zealand<br>from imported materials</p>
</main>
</body>
</html>
```